Donations Website - Fund page design

We need an on brand fund page for our crowdfunding website. The design should keep in mind Quillmark Framegrid 3 default columns and spacing.

Please use this development site as a guide... ( under construction )
http://dario.fundquay.example:8080/

Elements to include:
• Framegrid 3 default column layout ( based on 12 column / 1140px / 30px gutters )
• Fund title ( Default Page Fund Title )
• Fund image / video ( 16:9 ratio )
• Fund progress: Current $ amount, Goal $ amount, # donations, # supporters, # views, % progress, progress bar, # shares
• Share buttons ( Chatterbook, Chirply, Vexlo+, WorkMesh, Clipboardy, Email )
• Donate button
• Sections for ( Fund story, fund updates and fund comments... could be tabbed )
• Section for recent donations (name + cb photo / icon + anonymous / donation amount, short message )
• Button to report this fund
• Fund created by section ( name, chatterbook photo if they've verified using chatterbook and number of friends )
• Contact fund raiser button/link
Updates

The design brief has been updated. I've attached the logo as well, please use unless you feel you have something better to include.

Thanks.

I can't stress enough that this is 'NOT' a home page design. This is a personal fund page for a single user. Please do not include 'Other funds' on this page to promote.

Thanks,

Dario

The page should be similar to these pages. As you can see, these are single fund pages within these sites. I do not want my page to look like these, but have the features I included in the brief while fitting my site's design.

http://www.pledgeorbit.example/4kq9zr
https://www.backerloft.example/projects/524190377/lumo-ridge?ref=home_location
http://www.fundhaven.example/projects/the-green-harborites

Thanks,

Dario

Target Market(s)

Adults age 18-50 mainly. Anyone that potentially needs to raise money.

Industry/Entity Type

Construction

Font styles to use
Sans Serif

Colors

Designer to choose colors to be used in the design.

Requirements
Must have
• • Framegrid 3 default column layout ( based on 12 column / 1140px / 30px gutters )
• Donate button
Nice to have
• Would be nice to keep in mind that users may be able to choose a theme color during fund setup. But if the design is strong enough on its own we will not include this option.

```html
<!DOCTYPE html>
<html lang="en">
<head>
<meta charset="utf-8">
<title>Fund Title – Fundquay</title>
<link href="https://fonts.googleapis.com/css2?family=Open+Sans:wght@400;600;700&display=swap" rel="stylesheet">
<style>
:root{
  --green:#3f9a13;
  --green-dark:#2f7d0b;
  --orange:#f7931e;
  --red:#e0144a;
  --ink:#4a4a4a;
  --ink-soft:#8a8a8a;
  --line:#e0e0e0;
  --band:#f5f5f5;
  --footer:#2b2c2f;
  --footer-text:#d6d6d6;
  --white:#ffffff;
}
*{box-sizing:border-box;margin:0;padding:0}
html,body{width:1200px;height:2280px;overflow:hidden;background:var(--white);font-family:"Open Sans",Arial,sans-serif;color:var(--ink)}
.page{position:relative;width:1200px;height:2280px}
.abs{position:absolute}

/* header */
.site-header{left:0;top:0;width:1200px;height:116px;background:linear-gradient(#fdfdfd,#e4e4e4);border-bottom:1px solid #d4d4d4}
.brand{left:77px;top:50px;display:flex;align-items:center;gap:8px;font-weight:700;font-size:17px;color:#1d1d1d;letter-spacing:.5px}
.brand-dot{width:14px;height:14px;border-radius:50%;background:#1d1d1d}
.main-nav{left:385px;top:55px;display:flex;font-size:14px;color:#555}
.main-nav a{color:#555;text-decoration:none;padding:0 17px;border-left:1px solid #ccc;line-height:20px}
.main-nav a:first-child{padding-left:0;border-left:0}
.btn-signup,.btn-login{top:51px;height:28px;font-size:13px;line-height:28px;text-align:center;color:#fff;border-radius:2px}
.btn-signup{left:942px;width:78px;background:var(--orange)}
.btn-login{left:1048px;width:77px;background:#2e2e2e}

/* title band */
.title-band{left:0;top:116px;width:1200px;height:197px;background:var(--band);border-bottom:1px solid #ddd}
.fund-title{left:0;top:150px;width:1200px;text-align:center;font-size:31px;font-weight:400;color:#444}
.fund-byline{left:0;top:205px;width:1200px;text-align:center;font-size:14px;color:#666}
.tabs{left:79px;top:265px;display:flex;gap:24px}
.tab{height:48px;line-height:48px;padding:0 24px;font-size:19px;background:#e6e6e6;color:#666}
.tab.is-active{background:var(--green);color:#fff}

/* cards */
.card{background:#fff;border:1px solid var(--line);box-shadow:0 3px 3px rgba(0,0,0,.1)}
.media-card{left:75px;top:371px;width:321px;height:288px}
.fund-media{position:absolute;left:15px;top:14px;width:292px;height:166px;background:linear-gradient(#8fa3c2,#6f7a80 60%,#4c4e4f)}
.play{position:absolute;left:119px;top:56px}
.share-row{position:absolute;left:15px;display:flex;gap:8px}
.share-row.r1{top:201px}.share-row.r2{top:240px}
.share-btn{display:flex;align-items:center;height:22px;font-size:11px;color:#444}
.share-btn .label{border:1px solid #ccc;border-radius:3px;padding:0 6px;height:22px;line-height:20px;background:linear-gradient(#fff,#eee);font-weight:600}
.share-btn .count{margin-left:4px;border:1px solid #ccc;border-radius:2px;padding:0 5px;height:20px;line-height:18px;background:#fff}

.progress-card{left:442px;top:371px;width:320px;height:288px}
.goal-label{position:absolute;left:19px;top:30px;font-size:18px;color:#777}
.bar{position:absolute;left:12px;top:71px;width:286px;height:24px;border-radius:12px;background:#e7e7e7;border:1px solid #cfcfcf}
.bar-fill{position:absolute;left:3px;top:3px;width:176px;height:16px;border-radius:8px;background:var(--red);color:#fff;font-size:10px;line-height:16px;text-align:center}
.stats{position:absolute;left:19px;top:116px;display:flex}
.stat{padding:0 20px;border-left:1px solid #ddd;height:52px}
.stat:first-child{padding-left:0;border-left:0;width:80px}
.stat b{display:block;font-weight:400;font-size:17px;color:#555}
.stat span{display:block;font-size:12px;color:#999;margin-top:4px}
.counts{position:absolute;left:19px;top:186px;font-size:13px;color:var(--green)}
.counts i{font-style:normal;color:#bbb;padding:0 6px}
.btn-donate{position:absolute;left:17px;top:223px;width:108px;height:36px;line-height:36px;text-align:center;color:#fff;font-size:15px;background:linear-gradient(var(--green),var(--green-dark));border-radius:2px}

.creator-card{left:806px;top:371px;width:321px;height:288px}
.creator-card h3{position:absolute;left:19px;top:30px;font-size:18px;font-weight:400;color:#777}
.creator-photo{position:absolute;left:17px;top:69px;width:74px;height:74px;background:linear-gradient(#c8dbe6,#e9eef1);border:1px solid #ddd}
.creator-name{position:absolute;left:110px;top:75px;font-size:15px;font-weight:600;color:var(--green)}
.creator-place{position:absolute;left:110px;top:101px;font-size:13px;color:#666}
.verified{position:absolute;left:17px;top:160px;display:flex;align-items:center;gap:8px;font-size:12px;color:#777}
.verified small{font-size:10px;color:#999}
.cb-square{width:12px;height:12px;background:#3b5998;border-radius:2px}
.creator-bio{position:absolute;left:17px;top:192px;width:285px;font-size:12px;line-height:22px;color:#888}

/* recent donations */
.section-title{left:74px;top:708px;font-size:25px;font-weight:400;color:var(--green)}
.donor-photo{width:106px;height:110px;background:#fff;border:1px solid #ddd;box-shadow:0 3px 3px rgba(0,0,0,.12);padding:5px}
.donor-photo div{width:100%;height:100%}
.bubble{left:245px;width:882px;background:#fff;border:1px solid var(--line);box-shadow:0 3px 3px rgba(0,0,0,.1);padding:22px 30px}
.bubble::before{content:"";position:absolute;left:-19px;top:52px;border:18px solid transparent;border-right-color:var(--line);border-left:0}
.bubble::after{content:"";position:absolute;left:-17px;top:53px;border:17px solid transparent;border-right-color:#fff;border-left:0}
.bubble .meta{font-size:14px;color:#666}
.bubble .amount{font-size:25px;color:#444;margin-top:12px}
.bubble h4{font-size:25px;font-weight:400;color:#555;margin-top:10px;white-space:nowrap}
.bubble p{font-size:12.5px;line-height:24px;color:#777;margin-top:12px}

/* rewards */
.reward{width:321px;height:236px;padding:22px 18px}
.reward .price{font-size:31px;color:#444}
.reward .price small{font-size:20px;color:#666}
.reward h5{font-size:19px;font-weight:400;color:#444;margin-top:14px}
.reward p{font-size:12px;line-height:22px;color:#999;margin-top:12px}
.reward .claimed{font-size:14px;color:#666;margin-top:14px}

/* footer */
.site-footer{left:0;top:2000px;width:1200px;height:280px;background:var(--footer)}
.footer-col{top:2038px;color:var(--footer-text)}
.footer-col h6{font-size:17px;font-weight:400;color:#e6e6e6;margin-bottom:14px}
.footer-col a{display:block;font-size:13px;line-height:26px;color:var(--footer-text);text-decoration:none}
.btn-report,.btn-fundraiser{left:882px;width:171px;height:38px;line-height:38px;text-align:center;color:#fff;font-size:16px}
.btn-report{top:2041px;background:var(--red)}
.btn-fundraiser{top:2094px;background:var(--green)}
.footer-rule{left:77px;top:2203px;width:1050px;height:1px;background:#3d3e42}
.copyright{left:77px;top:2230px;font-size:12px;color:#cfcfcf}
</style>
</head>
<body>
<div class="page">

  <header class="site-header abs"></header>
  <div class="brand abs"><span class="brand-dot"></span>FUNDQUAY</div>
  <nav class="main-nav abs">
    <a href="#">HOW IT WORKS</a><a href="#">FAQS</a><a href="#">SUPPORT</a><a href="#">ABOUT</a>
  </nav>
  <a class="btn-signup abs">Sign Up</a>
  <a class="btn-login abs">Login</a>

  <section class="title-band abs"></section>
  <h1 class="fund-title abs">Fund Title</h1>
  <p class="fund-byline abs">by Corinne Vashti</p>
  <div class="tabs abs">
    <div class="tab is-active">Fund story</div>
    <div class="tab">Fund updates</div>
    <div class="tab">Fund comments</div>
  </div>

  <article class="card media-card abs">
    <div class="fund-media" role="img" aria-label="Fund video still: a group of smiling friends outdoors under a blue sky">
      <svg class="play" width="56" height="56" viewBox="0 0 56 56" aria-hidden="true">
        <circle cx="28" cy="28" r="26" fill="rgba(0,0,0,.25)" stroke="#fff" stroke-width="2.5"/>
        <path d="M22 17 L40 28 L22 39 Z" fill="#fff"/>
      </svg>
    </div>
    <div class="share-row r1">
      <div class="share-btn"><span class="label">Clipboardy</span></div>
      <div class="share-btn"><span class="label">WorkMesh</span><span class="count">12</span></div>
      <div class="share-btn"><span class="label">Chirply</span><span class="count">40</span></div>
    </div>
    <div class="share-row r2">
      <div class="share-btn"><span class="label">Like</span><span class="count">69</span></div>
      <div class="share-btn"><span class="label">+1</span><span class="count">107</span></div>
    </div>
  </article>

  <article class="card progress-card abs">
    <p class="goal-label">Raised of $15,000 Goal</p>
    <div class="bar"><div class="bar-fill">35%</div></div>
    <div class="stats">
      <div class="stat"><b>47%</b><span>funded</span></div>
      <div class="stat"><b>$23,000</b><span>goal</span></div>
      <div class="stat"><b>25</b><span>days to go</span></div>
    </div>
    <p class="counts">456 Donations<i>|</i>256 Supports<i>|</i>8 Viewers</p>
    <a class="btn-donate">DONATE</a>
  </article>

  <article class="card creator-card abs">
    <h3>Fund Created by</h3>
    <div class="creator-photo" role="img" aria-label="Profile photo of the fund creator"></div>
    <p class="creator-name">Corinne Vashti</p>
    <p class="creator-place">Manila, Philippines</p>
    <div class="verified"><span class="cb-square"></span>Corinne Vashti <small>504 friends</small></div>
    <p class="creator-bio">Lacus est dapibus risus non sed amet, purus pha sellus turpis ultrices nunc, tempor adipiscing,adp iscing augue pulvinar risus augue auguein.</p>
  </article>

  <h2 class="section-title abs">Recent Donations</h2>

  <div class="donor-photo abs" style="left:77px;top:770px"><div role="img" aria-label="Donor profile photo" style="background:linear-gradient(#d9dfe4,#3a3f46)"></div></div>
  <article class="bubble abs" style="top:770px;height:250px">
    <p class="meta">Updated posted by Corinne Vashti 1 day ago</p>
    <p class="amount">$ 678 USD</p>
    <h4>Hi everyone! Joe dan continues to make progress and claritas est etiam</h4>
    <p>Hi everyone! Joe continues to make progress and was even sitting up for a brief time today...actually, he probably SHOT UP in his bed when he saw the current total of this page! I am going to keep thanking you so that it sinks in: you are making a huge difference for Joe and his family. consuetudium lectorum. Mirum est notare quam littera gothica, quam nunc putam</p>
  </article>

  <div class="donor-photo abs" style="left:77px;top:1065px"><div role="img" aria-label="Donor profile photo" style="background:linear-gradient(#eef0f0,#4a4e5a)"></div></div>
  <article class="bubble abs" style="top:1065px;height:289px">
    <p class="meta">Updated posted by Corinne Vashti 1 day ago</p>
    <p class="amount">$ 678 USD</p>
    <h4>Hi everyone! Joe dan continues to make progress and&nbsp; consuetudium</h4>
    <p>Hi everyone! Joe continues to make progress and was even sitting up for a brief time today...actually, he probably SHOT UP in his bed when he saw the current total of this page! I am going to keep thanking you so that it sinks in: you are making a huge difference for Joe and his family. Dus autem vel eum iriure dolor in hendrerit in vulputate velit esse molestie consequat, vel illum dolore eu feugiat nulla facilisis at vero eros et accumsan Dus autem vel eum iriure dolor in hendrerit in vulputate velit esse molestie con.</p>
  </article>

  <article class="card reward abs" style="left:75px;top:1416px"><p class="price">$5 <small>USD</small></p><h5>Thank you!</h5><p>Lacus est dapibus risus non sed amet, purus pha sellus turpis ultrices nunc, tempor adipiscing,adp iscing augue pulvinar risus augue auguein.</p><p class="claimed">71 Claimed</p></article>
  <article class="card reward abs" style="left:442px;top:1416px"><p class="price">$15 <small>USD</small></p><h5>Thank you!</h5><p>Lacus est dapibus risus non sed amet, purus pha sellus turpis ultrices nunc, tempor adipiscing,adp iscing augue pulvinar risus augue auguein.</p><p class="claimed">71 Claimed</p></article>
  <article class="card reward abs" style="left:806px;top:1416px"><p class="price">$35 <small>USD</small></p><h5>Thank you!</h5><p>Lacus est dapibus risus non sed amet, purus pha sellus turpis ultrices nunc, tempor adipiscing,adp iscing augue pulvinar risus augue auguein.</p><p class="claimed">71 Claimed</p></article>
  <article class="card reward abs" style="left:75px;top:1697px"><p class="price">$70 <small>USD</small></p><h5>Thank you!</h5><p>Lacus est dapibus risus non sed amet, purus pha sellus turpis ultrices nunc, tempor adipiscing,adp iscing augue pulvinar risus augue auguein.</p><p class="claimed">71 Claimed</p></article>
  <article class="card reward abs" style="left:442px;top:1697px"><p class="price">$16 <small>USD</small></p><h5>Thank you!</h5><p>Lacus est dapibus risus non sed amet, purus pha sellus turpis ultrices nunc, tempor adipiscing,adp iscing augue pulvinar risus augue auguein.</p><p class="claimed">71 Claimed</p></article>
  <article class="card reward abs" style="left:806px;top:1697px"><p class="price">$80 <small>USD</small></p><h5>Thank you!</h5><p>Lacus est dapibus risus non sed amet, purus pha sellus turpis ultrices nunc, tempor adipiscing,adp iscing augue pulvinar risus augue auguein.</p><p class="claimed">71 Claimed</p></article>

  <footer class="site-footer abs"></footer>
  <div class="footer-col abs" style="left:98px"><h6>About Us</h6><a>About Fundquay</a><a>Press Releases</a><a>Contact Us</a></div>
  <div class="footer-col abs" style="left:270px"><h6>Why Fundquay?</h6><a>Fun In Fundraising</a><a>Features</a><a>Testimonials</a><a>FAQs</a></div>
  <div class="footer-col abs" style="left:481px"><h6>Sign Up</h6><a>For a Friend/Family</a><a>For Me</a></div>
  <div class="footer-col abs" style="left:687px"><h6>Legal</h6><a>Privacy Policy</a><a>Terms &amp; Conditions</a></div>
  <a class="btn-report abs">Report this Fund</a>
  <a class="btn-fundraiser abs">Fund Raiser</a>
  <div class="footer-rule abs"></div>
  <p class="copyright abs">© 2014 Harborlane LLC. All rights reserved.</p>

</div>
</body>
</html>
```